Social-Business Application (iOS)

App is very simillar to "Tandolo" from Vextromart

Please see the wireframes!

We need a design for application according to attached wireframes.
Social-Business application is a mobile app, that let's user to login, using Quorvix and browse through other users content (meme's). There are 2 home pages and 4 categories (displayed in wireframes). They are pretty simillar to each other. First one is called "Say Something" and the other one called "Ask Something". On "Say Something" page user is able to browse through meme's with pictures. There are several options to each meme, as well as reply to meme with your own meme.
"Ask Something" has only 2 differences.
1. There are always "?" in the end of each meme.
2. Only plain background with different colors are acceptable.
User is also able to create meme's to each home page and category.

There is no First or Last name display! Only following info should be displayed:
Location, Industry, Number of Quorvix contacts.

There is also a simple chat function, that provides the ability to chat with author of the meme. On the chat preview we will show the meme preview Instead of profile picture.

Please, ask your questions.
Updates

Please, send your examples.

Please check out "Tandolo" application for better understanding of the functionality and overall idea

https://apps.vextromart.com/store/apps/details?id=sh.tandolo

I will report to our admin, to change Designer Payment to Commited if we will have at least one screen example from you, guys.

Target Market(s)

regular users, business users.
Adult Audience, Professional Audience.

Industry/Entity Type

Business

Font styles to use
Other font styles liked:
• Helvetica Neue

Requirements
Must have
• Design must have all screens and elements that are displayed in attached photos (wireframes).
Flat style is required.
Following the iOS guidelines is required.
Nice to have
• Design example could show different ui colors for each of home pages ("Ask Something" and "Say Something") to easily indicate on what home page user is.
Should not have
• The design should not be overloaded and should not use serif fonts like Times New Roman.

```html
<!DOCTYPE html>
<html lang="en">
<head>
<meta charset="utf-8">
<title>Latest – Feed Screen</title>
<link rel="stylesheet" href="https://fonts.googleapis.com/css2?family=Roboto:wght@400;500;700&display=swap">
<style>
  :root {
    --stage: #232323;
    --brand: #684c7b;
    --brand-dark: #57406a;
    --panel-top: #e4e4e4;
    --panel-mid: #f7f7f7;
    --card: #ffffff;
    --label: #7d7d7d;
    --meta-icon: #a58fb2;
    --meta-text: #a3a3a3;
    --white: #ffffff;
    --dot-off: #ffffff;
  }
  * { box-sizing: border-box; margin: 0; padding: 0; }
  html, body {
    width: 1200px; height: 1152px; overflow: hidden;
    background: var(--stage);
    font-family: "Roboto", "Helvetica Neue", Arial, sans-serif;
  }
  .stage {
    position: absolute; left: 0; top: 0;
    width: 896px; height: 860px;
    transform: scale(1.3393); transform-origin: 0 0;
  }
  .screen {
    position: absolute; left: 221px; top: 47px;
    width: 436px; height: 775px;
    background: var(--brand);
    overflow: hidden;
  }
  .status-bar {
    position: absolute; left: 0; top: 0; width: 100%; height: 28px;
    color: var(--white); font-size: 15px;
  }
  .status-bar .carrier { position: absolute; left: 9px; top: 5px; display: flex; align-items: center; gap: 6px; }
  .signal { display: flex; gap: 2px; }
  .signal i { width: 7px; height: 7px; border-radius: 50%; border: 1px solid var(--white); display: block; }
  .signal i.on { background: var(--white); }
  .status-bar .wifi { position: absolute; left: 132px; top: 6px; }
  .status-bar .time { position: absolute; left: 0; right: 0; top: 5px; text-align: center; }
  .status-bar .battery { position: absolute; right: 7px; top: 5px; display: flex; align-items: center; gap: 5px; }
  .battery-cell { width: 30px; height: 13px; border: 1px solid var(--white); border-radius: 3px; padding: 1px; position: relative; }
  .battery-cell::before { content: ""; display: block; width: 100%; height: 100%; background: var(--white); border-radius: 1px; }
  .battery-cell::after { content: ""; position: absolute; right: -4px; top: 3px; width: 2px; height: 5px; background: var(--white); border-radius: 0 1px 1px 0; }

  .nav-bar { position: absolute; left: 0; top: 28px; width: 100%; height: 60px; }
  .nav-bar .title {
    position: absolute; left: 0; right: 0; top: 16px; text-align: center;
    color: var(--white); font-size: 20px; font-weight: 700;
  }
  .nav-bar .menu { position: absolute; left: 20px; top: 19px; }
  .nav-bar .inbox { position: absolute; right: 16px; top: 20px; }

  .feed-panel {
    position: absolute; left: 7px; right: 7px; top: 88px; bottom: 0;
    background: linear-gradient(180deg, var(--panel-top) 0%, var(--panel-mid) 40px, #f1f1f1 60%, #e9e9e9 100%);
    border-radius: 0 0 0 0;
  }
  .pager {
    position: absolute; left: 0; right: 0; top: 103px;
    display: flex; justify-content: center; gap: 4px;
  }
  .pager i { width: 9px; height: 9px; border-radius: 50%; background: var(--dot-off); display: block; box-shadow: 0 0 1px rgba(0,0,0,.15); }
  .pager i.active { background: var(--brand); }

  .edge-arrow { position: absolute; top: 397px; width: 0; height: 0; border-top: 8px solid transparent; border-bottom: 8px solid transparent; }
  .edge-arrow.left { left: 7px; border-right: 6px solid var(--panel-mid); }
  .edge-arrow.right { right: 1px; border-left: 6px solid var(--panel-mid); }

  .post-card {
    position: absolute; width: 199px; height: 245px;
    background: var(--card);
    box-shadow: 0 1px 2px rgba(0,0,0,.12);
  }
  .post-card .meta-line {
    height: 35px; padding: 9px 10px 0; font-size: 15px; color: var(--label);
  }
  .post-card .media { height: 174px; }
  .post-card .stats {
    height: 36px; display: flex; justify-content: center; align-items: center; gap: 10px;
    font-size: 14px; color: var(--meta-text);
  }
  .stats span { display: flex; align-items: center; gap: 3px; }

  .col-left { left: 12px; }
  .col-right { left: 224px; }
  .row-1 { top: 129px; }
  .row-2 { top: 391px; }
  .row-3 { top: 655px; }

  .media-jelly { background: radial-gradient(circle at 45% 45%, #f4c7cc 0%, #e59aa6 35%, #c9b7b7 65%, #8fc1bd 100%); }
  .media-nebula { background: radial-gradient(circle at 40% 45%, #3a1f4e 0%, #2f5f86 35%, #b23a3a 75%, #6b1f2b 100%); }
  .media-tulips { background: linear-gradient(180deg, #c8142c 0%, #a8102a 50%, #6c1019 100%); }
  .media-night { background: linear-gradient(180deg, #2b38b0 0%, #2d2f8c 35%, #c99a2f 55%, #2d2a7a 75%, #3d3f8e 100%); }

  .say-button {
    position: absolute; left: 37px; top: 704px; width: 362px; height: 59px;
    background: var(--brand); border: 2px solid var(--white); border-radius: 7px;
    box-shadow: 0 2px 4px rgba(0,0,0,.25);
    display: flex; align-items: center; justify-content: center; gap: 10px;
    color: var(--white); font-size: 20px; font-weight: 700;
  }
</style>
</head>
<body>
<div class="stage">
  <main class="screen">
    <div class="status-bar">
      <div class="carrier"><span class="signal"><i class="on"></i><i class="on"></i><i class="on"></i><i></i><i></i></span>Norvel</div>
      <svg class="wifi" width="17" height="13" viewBox="0 0 17 13"><path d="M1 5a11 11 0 0 1 15 0M3.5 7.5a7.5 7.5 0 0 1 10 0M6 10a4 4 0 0 1 5 0" fill="none" stroke="#fff" stroke-width="1.8" stroke-linecap="round"/><circle cx="8.5" cy="12" r="1.2" fill="#fff"/></svg>
      <div class="time">4:21 PM</div>
      <div class="battery">100%<span class="battery-cell"></span></div>
    </div>

    <header class="nav-bar">
      <svg class="menu" width="22" height="20" viewBox="0 0 22 20" fill="#fff"><rect x="0" y="1" width="4" height="3"/><rect x="6" y="1" width="16" height="3"/><rect x="0" y="6" width="4" height="3"/><rect x="6" y="6" width="16" height="3"/><rect x="0" y="11" width="4" height="3"/><rect x="6" y="11" width="16" height="3"/><rect x="0" y="16" width="4" height="3"/><rect x="6" y="16" width="16" height="3"/></svg>
      <h1 class="title">Latest</h1>
      <svg class="inbox" width="27" height="20" viewBox="0 0 27 20"><rect x="1" y="1" width="25" height="18" rx="1.5" fill="none" stroke="#fff" stroke-width="2"/><path d="M1.5 2 13.5 12 25.5 2M1.5 18 10.5 9.5M25.5 18 16.5 9.5" fill="none" stroke="#fff" stroke-width="2"/></svg>
    </header>

    <section class="feed-panel"></section>
    <span class="edge-arrow left"></span>
    <span class="edge-arrow right"></span>

    <div class="pager"><i class="active"></i><i></i><i></i><i></i></div>

    <article class="post-card col-left row-1">
      <div class="meta-line">Location</div>
      <div class="media media-jelly" role="img" aria-label="Photo of pink jellyfish drifting in teal water"></div>
      <div class="stats">
        <span><svg width="15" height="15" viewBox="0 0 15 15"><circle cx="7.5" cy="7.5" r="7" fill="#a58fb2"/><path d="M7.5 3.5v4.5l3 1.5" stroke="#fff" stroke-width="1.6" fill="none"/></svg>5m</span>
        <span><svg width="16" height="14" viewBox="0 0 16 14"><path d="M8 13.5 1.5 7A3.8 3.8 0 0 1 8 2.3 3.8 3.8 0 0 1 14.5 7Z" fill="#a58fb2"/></svg>0</span>
        <span><svg width="16" height="14" viewBox="0 0 16 14"><path d="M8 1C4 1 1 3.3 1 6.2c0 1.5.8 2.8 2 3.7L2.2 13l3.6-2c.7.2 1.4.3 2.2.3 4 0 7-2.3 7-5.1S12 1 8 1Z" fill="#a58fb2"/></svg>31</span>
      </div>
    </article>

    <article class="post-card col-right row-1">
      <div class="meta-line">Location, other info</div>
      <div class="media media-nebula" role="img" aria-label="Photo of a colourful space nebula with stars"></div>
      <div class="stats">
        <span><svg width="15" height="15" viewBox="0 0 15 15"><circle cx="7.5" cy="7.5" r="7" fill="#a58fb2"/><path d="M7.5 3.5v4.5l3 1.5" stroke="#fff" stroke-width="1.6" fill="none"/></svg>5m</span>
        <span><svg width="16" height="14" viewBox="0 0 16 14"><path d="M8 13.5 1.5 7A3.8 3.8 0 0 1 8 2.3 3.8 3.8 0 0 1 14.5 7Z" fill="#a58fb2"/></svg>0</span>
        <span><svg width="16" height="14" viewBox="0 0 16 14"><path d="M8 1C4 1 1 3.3 1 6.2c0 1.5.8 2.8 2 3.7L2.2 13l3.6-2c.7.2 1.4.3 2.2.3 4 0 7-2.3 7-5.1S12 1 8 1Z" fill="#a58fb2"/></svg>31</span>
      </div>
    </article>

    <article class="post-card col-left row-2">
      <div class="meta-line">Location</div>
      <div class="media media-tulips" role="img" aria-label="Photo of a field of red tulips with a single white tulip"></div>
      <div class="stats">
        <span><svg width="15" height="15" viewBox="0 0 15 15"><circle cx="7.5" cy="7.5" r="7" fill="#a58fb2"/><path d="M7.5 3.5v4.5l3 1.5" stroke="#fff" stroke-width="1.6" fill="none"/></svg>5m</span>
        <span><svg width="16" height="14" viewBox="0 0 16 14"><path d="M8 13.5 1.5 7A3.8 3.8 0 0 1 8 2.3 3.8 3.8 0 0 1 14.5 7Z" fill="#a58fb2"/></svg>0</span>
        <span><svg width="16" height="14" viewBox="0 0 16 14"><path d="M8 1C4 1 1 3.3 1 6.2c0 1.5.8 2.8 2 3.7L2.2 13l3.6-2c.7.2 1.4.3 2.2.3 4 0 7-2.3 7-5.1S12 1 8 1Z" fill="#a58fb2"/></svg>31</span>
      </div>
    </article>

    <article class="post-card col-right row-2">
      <div class="meta-line">Location, other info</div>
      <div class="media media-night" role="img" aria-label="Painting of a night river with lights reflected and boats"></div>
      <div class="stats">
        <span><svg width="15" height="15" viewBox="0 0 15 15"><circle cx="7.5" cy="7.5" r="7" fill="#a58fb2"/><path d="M7.5 3.5v4.5l3 1.5" stroke="#fff" stroke-width="1.6" fill="none"/></svg>5m</span>
        <span><svg width="16" height="14" viewBox="0 0 16 14"><path d="M8 13.5 1.5 7A3.8 3.8 0 0 1 8 2.3 3.8 3.8 0 0 1 14.5 7Z" fill="#a58fb2"/></svg>0</span>
        <span><svg width="16" height="14" viewBox="0 0 16 14"><path d="M8 1C4 1 1 3.3 1 6.2c0 1.5.8 2.8 2 3.7L2.2 13l3.6-2c.7.2 1.4.3 2.2.3 4 0 7-2.3 7-5.1S12 1 8 1Z" fill="#a58fb2"/></svg>31</span>
      </div>
    </article>

    <article class="post-card col-left row-3">
      <div class="meta-line">Location</div>
      <div class="media media-jelly" role="img" aria-label="Photo of pink jellyfish drifting in teal water"></div>
    </article>

    <article class="post-card col-right row-3">
      <div class="meta-line">Location, other info</div>
      <div class="media media-nebula" role="img" aria-label="Photo of a colourful space nebula with stars"></div>
    </article>

    <div class="say-button">
      <svg width="34" height="32" viewBox="0 0 34 32"><path d="M17 2C8.7 2 2 7.6 2 14.5c0 3.6 1.8 6.8 4.7 9.1L5 30l7.3-3.6c1.5.4 3.1.6 4.7.6 8.3 0 15-5.6 15-12.5S25.3 2 17 2Z" fill="#fff"/><rect x="10" y="10" width="14" height="2.4" fill="#684c7b"/><rect x="10" y="14" width="14" height="2.4" fill="#684c7b"/><rect x="10" y="18" width="10" height="2.4" fill="#684c7b"/></svg>
      Say something
    </div>
  </main>
</div>
</body>
</html>
```